Business Card Design

Hello,
I try and keep my business card fresh and current. So about every year i get a new one. This year I'd like something with a white background and black lettering.
Before you start - I do not want my phone number or any other description on the card other than my url and my email.

I'd like a double sided business card with
TobFarnsby.com on one side

and

Tob@TobFarnsby.com on the other side of the card

Thinking very minimalistic and modern.
I don't have a particular font i mind or how to capitalize my name or website. This card will lead people to my new website that is being designed to showcase my photography and music.

* Initial thought was the front side of the card having a grid-like pattern built out of dashes or periods, with my website sitting within the pattern and on the back side my email on a stark white background. But that might look completely lame - haha.

I'm looking forward to seeing what you come up with.

thank you,
- tob farnsby

Reason: Want to spend some more time with the designs and add a little $. thanks for all the designs - tob

Wanted to add a little $ and spend some more time with the designs.

big thanks to all who have submitted work 

- tob

Industry/Entity Type

Business

Contact Information for Business Card

www.tobfarnsby.com
tob@tobfarnsby.com

Colors
000000
ffffff

Requirements
Must have
• tobfarnsby.com
tob@tobfarnsby.com
Should not have
• phone number
any description of what i do, photography or music

```html
<!DOCTYPE html>
<html lang="en">
<head>
<meta charset="utf-8">
<title>Tob Farnsby — Business Card</title>
<link rel="stylesheet" href="https://fonts.googleapis.com/css2?family=Dancing+Script:wght@500;600&display=swap">
<style>
  :root {
    --backdrop-dark: #050505;
    --backdrop-mid: #262626;
    --card-base: #161616;
    --panel-light: #f1f3f3;
    --panel-light-shade: #c9cdcd;
    --panel-mid: #c2c6c6;
    --panel-mid-shade: #aeb3b3;
    --ink: #262626;
    --ink-soft: #8a8e8e;
    --icon-tone: #3a3a3a;
  }
  html, body {
    margin: 0;
    padding: 0;
    width: 1200px;
    height: 900px;
    overflow: hidden;
  }
  body {
    background: radial-gradient(ellipse at 50% 50%, var(--backdrop-mid) 0%, var(--backdrop-dark) 75%);
  }
  .card {
    position: absolute;
    width: 630px;
    height: 358px;
    display: block;
  }
  .card--front { left: 285px; top: 60px; }
  .card--back  { left: 292px; top: 481px; }
  .script {
    font-family: "Dancing Script", cursive;
    font-weight: 600;
  }
  .contact-line { fill: var(--ink); font-size: 33px; }
  .monogram { fill: var(--ink-soft); font-size: 76px; }
  .contact-line--soft { fill: var(--ink-soft); font-size: 23px; }
</style>
</head>
<body>

<svg class="card card--front" viewBox="0 0 630 358" xmlns="http://www.w3.org/2000/svg">
  <defs>
    <linearGradient id="lightPanel" x1="0" y1="0" x2="0.6" y2="1">
      <stop offset="0" stop-color="#fbfcfc"/>
      <stop offset="1" stop-color="#c8cccc"/>
    </linearGradient>
    <linearGradient id="midPanel" x1="0" y1="0" x2="1" y2="1">
      <stop offset="0" stop-color="#cdd1d1"/>
      <stop offset="1" stop-color="#b9bebe"/>
    </linearGradient>
    <radialGradient id="topWell" cx="0.5" cy="0.75" r="0.7">
      <stop offset="0" stop-color="#ffffff"/>
      <stop offset="1" stop-color="#5e6262"/>
    </radialGradient>
    <linearGradient id="bottomWell" x1="0" y1="0" x2="0" y2="1">
      <stop offset="0" stop-color="#eef0f0"/>
      <stop offset="1" stop-color="#b4b9b9"/>
    </linearGradient>
    <filter id="drop" x="-10%" y="-10%" width="120%" height="120%">
      <feDropShadow dx="3" dy="3" stdDeviation="4" flood-color="#000" flood-opacity="0.45"/>
    </filter>
  </defs>
  <rect class="card-base" width="630" height="358" fill="var(--card-base)"/>
  <polygon class="panel panel--corner" points="490,0 630,0 630,180 462,28" fill="url(#lightPanel)"/>
  <polygon class="panel panel--mid" points="350,150 466,32 630,196 630,300 560,358 455,358" fill="url(#midPanel)" filter="url(#drop)"/>
  <polygon class="panel panel--well-top" points="215,0 470,0 342,130" fill="url(#topWell)"/>
  <polygon class="panel panel--large" points="0,92 92,0 215,0 465,265 372,358 0,358" fill="url(#lightPanel)" filter="url(#drop)"/>
  <polygon class="panel panel--well-bottom" points="205,358 325,245 455,358" fill="url(#bottomWell)" filter="url(#drop)"/>
  <rect class="icon-slot icon-slot--camera" x="315" y="25" width="60" height="45" rx="6" fill="var(--icon-tone)" role="img" aria-label="Camera icon"/>
  <rect class="icon-slot icon-slot--music" x="262" y="305" width="90" height="38" rx="4" fill="var(--panel-mid-shade)" role="img" aria-label="Music staff with notes"/>
  <text class="script contact-line" x="22" y="206">Tob@TobFarnsby.com</text>
  <text class="script monogram" x="422" y="238">Tob</text>
</svg>

<svg class="card card--back" viewBox="0 0 630 358" xmlns="http://www.w3.org/2000/svg">
  <rect class="card-base" width="630" height="358" fill="var(--card-base)"/>
  <polygon class="panel panel--corner" points="490,0 630,0 630,180 462,28" fill="url(#lightPanel)"/>
  <polygon class="panel panel--mid" points="350,150 466,32 630,196 630,300 560,358 455,358" fill="url(#midPanel)" filter="url(#drop)"/>
  <polygon class="panel panel--well-top" points="215,0 470,0 342,130" fill="url(#topWell)"/>
  <polygon class="panel panel--large" points="0,92 92,0 215,0 465,265 372,358 0,358" fill="url(#lightPanel)" filter="url(#drop)"/>
  <polygon class="panel panel--well-bottom" points="205,358 325,245 455,358" fill="url(#bottomWell)" filter="url(#drop)"/>
  <rect class="icon-slot icon-slot--camera" x="315" y="25" width="60" height="45" rx="6" fill="var(--icon-tone)" role="img" aria-label="Camera icon"/>
  <rect class="icon-slot icon-slot--music" x="262" y="305" width="90" height="38" rx="4" fill="var(--panel-mid-shade)" role="img" aria-label="Music staff with notes"/>
  <text class="script contact-line" x="48" y="196">TobFarnsby.com</text>
  <text class="script contact-line--soft" x="446" y="220">TobFarnsby.com</text>
</svg>

</body>
</html>
```